Transit Van Vehicle Wrap for Fenwick Meadow Gardens

We need to wrap two of our transit vans. One is a replacement. The old wrap had a back patio scene with patio furniture and lanscaping. Im not sure this is what we want moving forward. I want people to easily identify it is Fenwick Meadow Gardens when they look at the vehicle. Most recently we have wrapped our landscape trailers black, however with the base color being white and not wanting to wrap all of the vehicle, Im not sure black background is the way to go. We've also considered using 3 or 4 picture windows and a subtitle to describe what we do. We can to list words like Container Gardening, Backyard Patios, Houseplants, Plant Doctors, etc. instead of using department names to tell people what we do. We would like to use more specific words and words that formulate an image in your mind when you say it. Needs to have our logo in it. Sides and Rear doors. Rear should be logo with words or services listed. The sides could be the same or images. Ive attached two logos, one meant to be used overtop of darker background. We are a retail lifestyle garden center and landscape design build company, selling annuals, perennial, trees shrubs, lawn care items, gardening tools, house plants, pottery, patio furniture, mens and womens apparel and accessories, christmas decor and trees, lorne candles and other home fragrence, seasonal home decor and more. Visit fenwickmeadowgardens.com to see it all.

Target Market(s)

Home Owners in their 40s to 50s

Industry/Entity Type

lifestyle garden center and landscape firm

Requirements
Must have
• company logo and words describing what we do.

```html
<!DOCTYPE html>
<html lang="en">
<head>
<meta charset="utf-8">
<title>Fenwick Meadow Gardens – Transit Van Wrap</title>
<link rel="stylesheet" href="https://fonts.googleapis.com/css2?family=Caveat:wght@500&family=Great+Vibes&family=Roboto+Condensed:wght@300;400&display=swap">
<style>
  :root {
    --canvas: #ececec;
    --wrap-black: #1d1d1f;
    --window-black: #111113;
    --seam: #2c2c2f;
    --leaf-green: #a4cc55;
    --text-white: #f2f2f2;
    --text-grey: #b9b9b9;
    --petal-yellow: #f1d23c;
    --seed-brown: #8a6a3c;
  }
  * { margin: 0; padding: 0; box-sizing: border-box; }
  html, body { width: 1200px; height: 1200px; overflow: hidden; background: var(--canvas); }
  .artboard { position: relative; width: 1200px; height: 1200px; }

  .brand-name {
    font-family: "Roboto Condensed", sans-serif; font-weight: 400;
    color: var(--leaf-green); text-transform: uppercase;
    display: flex; align-items: center; gap: 8px; justify-content: center; white-space: nowrap;
  }
  .brand-name .brand-dot { width: 12px; height: 12px; border-radius: 50%; background: var(--petal-yellow); flex: none; }

  /* Rear doors */
  .rear-doors {
    position: absolute; left: 370px; top: 60px; width: 460px; height: 480px;
    background: var(--wrap-black); border-radius: 40px 40px 18px 18px; overflow: hidden;
  }
  .rear-doors .rear-window {
    position: absolute; left: 30px; top: 30px; width: 400px; height: 190px;
    background: var(--window-black); border-radius: 30px 30px 10px 10px;
  }
  .rear-doors .door-seam { position: absolute; left: 229px; top: 0; width: 2px; height: 100%; background: var(--seam); }
  .rear-doors .brand-name { position: absolute; left: 0; right: 0; top: 62px; font-size: 22px; letter-spacing: 1.5px; }
  .rear-tagline {
    position: absolute; left: 0; right: 0; top: 100px; text-align: center;
    font-family: "Caveat", cursive; font-weight: 500; font-size: 25px; line-height: 1.05; color: var(--text-white);
  }
  .rear-services {
    position: absolute; left: 58px; top: 232px; font-family: "Roboto Condensed", sans-serif; color: var(--text-grey);
  }
  .rear-services h3 { font-weight: 300; font-size: 14px; color: var(--leaf-green); margin-bottom: 2px; }
  .rear-services li { list-style: none; font-size: 7.5px; line-height: 1.4; }
  .rear-phone {
    position: absolute; left: 262px; top: 252px; font-family: "Roboto Condensed", sans-serif; font-weight: 300;
    font-size: 13px; color: var(--text-white); white-space: nowrap;
  }
  .rear-phone strong { font-weight: 300; font-size: 18px; color: var(--leaf-green); margin-left: 4px; }
  .rear-handle { position: absolute; left: 250px; top: 322px; width: 48px; height: 10px; border-radius: 5px; background: #2e2e31; }
  .rear-plate { position: absolute; left: 55px; top: 404px; width: 110px; height: 24px; background: #f7f7f7; border-radius: 2px; }
  .rear-sunflower {
    position: absolute; left: 232px; top: 392px; width: 220px; height: 110px; border-radius: 90px 90px 0 0;
    background: linear-gradient(180deg, var(--petal-yellow) 0%, #d4b043 55%, var(--seed-brown) 100%);
  }

  /* Side panel */
  .side-panel {
    position: absolute; left: 90px; top: 620px; width: 1020px; height: 440px;
    background: var(--wrap-black); border-radius: 60px 30px 18px 18px; overflow: hidden;
  }
  .side-panel .side-window {
    position: absolute; left: 150px; top: 40px; width: 270px; height: 150px;
    background: var(--window-black); border-radius: 14px;
  }
  .side-panel .brand-name { position: absolute; left: 150px; top: 102px; width: 270px; font-size: 18px; letter-spacing: 1px; }
  .side-slogan {
    position: absolute; left: 150px; top: 194px; font-family: "Great Vibes", cursive;
    font-size: 58px; color: var(--text-white); white-space: nowrap;
  }
  .side-phone {
    position: absolute; left: 150px; top: 286px; font-family: "Roboto Condensed", sans-serif; font-weight: 300;
    font-size: 34px; color: var(--text-white); white-space: nowrap;
  }
  .side-phone strong { font-weight: 300; font-size: 60px; color: var(--leaf-green); margin-left: 10px; vertical-align: -6px; }
  .side-web {
    position: absolute; left: 560px; top: 368px; font-family: "Roboto Condensed", sans-serif; font-weight: 300;
    font-size: 20px; color: var(--text-grey);
  }
  .side-services {
    position: absolute; left: 560px; top: 48px; font-family: "Roboto Condensed", sans-serif; font-weight: 300;
  }
  .side-services h3 { font-weight: 300; font-size: 26px; color: var(--leaf-green); margin-bottom: 4px; }
  .side-services li { list-style: none; font-size: 21px; line-height: 1.35; color: var(--text-white); }
  .side-sunflower {
    position: absolute; left: 840px; top: 10px; width: 180px; height: 300px; border-radius: 60px 0 0 60px;
    background: linear-gradient(90deg, var(--petal-yellow) 0%, #d4b043 60%, var(--seed-brown) 100%);
  }
</style>
</head>
<body>
<main class="artboard">

  <section class="rear-doors" aria-label="Rear doors wrap">
    <div class="rear-window"></div>
    <div class="door-seam"></div>
    <div class="brand-name"><span class="brand-dot"></span>Fenwick Meadow Gardens</div>
    <p class="rear-tagline">lifestyle garden center and<br>landscape design build company.</p>
    <div class="rear-services">
      <h3>Services</h3>
      <ul>
        <li>Spring annuals</li>
        <li>Perennials</li>
        <li>Trees &amp; shrubs</li>
        <li>Lawn care items</li>
        <li>Gardening tools</li>
        <li>House plants</li>
        <li>Pottery</li>
        <li>Patio furniture</li>
        <li>Apparel and accessories</li>
        <li>Christmas decor and trees</li>
        <li>Lorne candles and home fragrance</li>
        <li>Seasonal home decor</li>
      </ul>
    </div>
    <p class="rear-phone">Call us <strong>215-555-0148</strong></p>
    <div class="rear-handle"></div>
    <div class="rear-plate"></div>
    <div class="rear-sunflower" role="img" aria-label="Illustrated yellow sunflower rising from the lower door edge"></div>
  </section>

  <section class="side-panel" aria-label="Side wrap">
    <div class="side-window"></div>
    <div class="brand-name"><span class="brand-dot"></span>Fenwick Meadow Gardens</div>
    <p class="side-slogan">Spring It On</p>
    <p class="side-phone">Call us <strong>215-555-0148</strong></p>
    <p class="side-web">fenwickmeadowgardens.com</p>
    <div class="side-services">
      <h3>Services</h3>
      <ul>
        <li>.Container Gardening</li>
        <li>.Backyard Patios</li>
        <li>.Houseplants</li>
        <li>.Plant Doctors</li>
      </ul>
    </div>
    <div class="side-sunflower" role="img" aria-label="Large illustrated sunflower wrapping around the rear corner"></div>
  </section>

</main>
</body>
</html>
```